Business card design needed

Riverstone Limited is a management company that manages Riverstone Brisk Journeys ticketing agency for Skylark Aero and Kumbora Valley Printers a small printing company in Mt Hagen Papua New Guinea.

Industry/Entity Type

Printing

Contact Information for Business Card

Riverstone Limited
Rosalind Kewatego
P: +675 318 4057 F: +675 318 4093
Po Box 371 Mt Hagen WHP
Papua New Guinea
E: rosalind@riverstonelimited-example.com

Logo Text

Riverstone Limited

Logo styles of interest
Emblem Logo
Requirements
Must have
• Bottom Left hand corner of business card to have a small globe with Papua New Guinea in the middle Australia showing at the bottom and Riverstone walking from PNG up and spiralling down the globe (like an ANT Trail) than down and walking along the bottom of business card with Carrying A Quiet Welcome in the middle of the card. CARD TO BE DONE IN TWO COLORS Black background and Electric Blue writing
Nice to have
• Printing Both sides
on Front as per above details
on Back, all to be Centered

Riverstone Limited
Managing
Riverstone Brisk Journeys
+675 318 4057
Kumbora Valley Printers
+675 318 7246

```html
<!DOCTYPE html>
<html lang="en">
<head>
<meta charset="utf-8">
<title>Riverstone Limited — Business Card</title>
<link rel="stylesheet" href="https://fonts.googleapis.com/css2?family=Arimo:wght@400;500;700&display=swap">
<style>
  :root {
    --card-bg: #000000;
    --electric-blue: #1f8fff;
    --globe-light: #3aa6ff;
    --globe-dark: #0a3f8c;
  }
  html, body {
    margin: 0;
    padding: 0;
    overflow: hidden;
    background: var(--card-bg);
  }
  .business-card {
    position: relative;
    width: 1200px;
    height: 693px;
    background: var(--card-bg);
    overflow: hidden;
    font-family: "Arimo", Arial, sans-serif;
    color: var(--electric-blue);
  }
  .brand-name {
    position: absolute;
    left: 70px;
    top: 96px;
    margin: 0;
    font-size: 46px;
    font-weight: 700;
    line-height: 1;
    letter-spacing: -0.5px;
    color: var(--electric-blue);
  }
  .trail {
    position: absolute;
    left: 0;
    top: 0;
    width: 1200px;
    height: 693px;
    pointer-events: none;
  }
  .trail__path {
    fill: none;
    stroke: var(--electric-blue);
    stroke-width: 5;
    stroke-linecap: round;
    stroke-dasharray: 2 16;
  }
  .globe {
    position: absolute;
    left: 60px;
    top: 395px;
    width: 230px;
    height: 230px;
    border-radius: 50%;
    background: radial-gradient(circle at 38% 34%, var(--globe-light), var(--globe-dark));
  }
  .tagline {
    position: absolute;
    left: 0;
    right: 0;
    top: 596px;
    margin: 0;
    text-align: center;
    font-size: 30px;
    font-weight: 500;
    letter-spacing: 0.5px;
    color: var(--electric-blue);
  }
  .contact {
    position: absolute;
    left: 695px;
    top: 232px;
  }
  .contact__lines,
  .contact__address {
    margin: 0;
    padding: 0;
    list-style: none;
  }
  .contact__lines li {
    font-size: 28px;
    font-weight: 500;
    line-height: 33px;
    letter-spacing: -0.2px;
  }
  .contact__lines .contact__email {
    font-size: 24px;
  }
  .contact__address {
    margin-top: 16px;
  }
  .contact__address li {
    font-size: 30px;
    font-weight: 500;
    line-height: 34px;
    letter-spacing: -0.2px;
  }
</style>
</head>
<body>
  <div class="business-card">
    <p class="brand-name">Riverstone Limited</p>

    <svg class="trail" viewBox="0 0 1200 693" aria-hidden="true">
      <path class="trail__path"
        d="M 175 500 C 230 470 265 420 230 405 C 190 385 95 420 90 500 C 85 590 170 650 260 660 C 450 672 800 665 1160 662"/>
    </svg>

    <div class="globe" role="img" aria-label="Small globe with Papua New Guinea in the centre and Australia at the bottom"></div>

    <p class="tagline">Carrying A Quiet Welcome</p>

    <div class="contact">
      <ul class="contact__lines">
        <li>P: +675 318 4057</li>
        <li>F: +675 318 4093</li>
        <li class="contact__email">rosalind@riverstonelimited-example.com</li>
      </ul>
      <ul class="contact__address">
        <li>Riverstone Limited</li>
        <li>Rosalind Kewatego,</li>
        <li>Po Box 371 Mt Hagen WHP</li>
        <li>Papua New Guinea</li>
      </ul>
    </div>
  </div>
</body>
</html>
```